Property Developer - Simple yet Sophisticated and Sharp Business Card

We are a medium sized property developer involved mainly in townhouse developments and land subdivisions.

The company is looking for a simple, sharp and sophisticated business card that will be given to contractors, land owners, financiers etc and thus will need to look professional.

Property development related graphics and art can be used, however the card is not to be too "busy" or crowded. Our company name is KL Estates which could possibly be incorporated into the graphics or artwork.

Single sided and/or double sided designs will be acceptable.

A Simple, Sophisticated, Sharp design please!

Good Luck !

```html
<!DOCTYPE html>
<html lang="en">
<head>
<meta charset="utf-8">
<title>KL Estates – Business Card</title>
<link rel="stylesheet" href="https://fonts.googleapis.com/css2?family=Merriweather:wght@700;900&family=Arimo:wght@400;700&display=swap">
<style>
  :root {
    --stage: #2b2b2d;
    --card-edge: #f4f4f4;
    --panel-light: #cfcfcf;
    --panel-dark: #bcbcbc;
    --band: #8f8f8f;
    --band-edge: #a6a6a6;
    --ink: #1c1c1c;
    --mark: rgba(0, 0, 0, 0.09);
  }
  * { box-sizing: border-box; margin: 0; padding: 0; }
  html, body {
    width: 1200px;
    height: 1052px;
    overflow: hidden;
    background: var(--stage);
  }
  .card {
    position: absolute;
    width: 720px;
    height: 412px;
    background: var(--card-edge);
    box-shadow: 0 10px 30px rgba(0, 0, 0, 0.45);
    overflow: hidden;
  }
  .card--front { left: 80px; top: 70px; }
  .card--back { left: 400px; top: 570px; }

  .card__band {
    position: absolute;
    left: 0;
    width: 100%;
    background: var(--band-edge);
  }
  .card__panel {
    position: absolute;
    inset: 24px;
    border-radius: 30px;
    background: linear-gradient(160deg, var(--panel-light), var(--panel-dark));
    overflow: hidden;
  }
  .card__panel .card__band { background: var(--band); }

  /* Front */
  .card--front .card__band { top: 140px; height: 104px; }
  .card--front .card__panel .card__band { top: 116px; }
  .front__name {
    position: absolute;
    left: 76px;
    top: 128px;
    font-family: "Merriweather", Georgia, serif;
    font-weight: 900;
    font-size: 58px;
    letter-spacing: 0.5px;
    color: var(--ink);
  }
  .front__email {
    position: absolute;
    right: 70px;
    top: 226px;
    font-family: "Arimo", Arial, sans-serif;
    font-size: 18px;
    color: var(--ink);
  }

  /* Back */
  .card--back > .card__band { top: 168px; height: 84px; }
  .back__mark {
    position: absolute;
    left: 54px;
    top: 34px;
    width: 96px;
    height: 96px;
    background: var(--mark);
  }
  .back__name {
    position: absolute;
    left: 44px;
    top: 30px;
    font-family: "Merriweather", Georgia, serif;
    font-weight: 900;
    font-size: 34px;
    color: var(--ink);
  }
  .back__contact {
    position: absolute;
    right: 34px;
    bottom: 22px;
    text-align: right;
    font-family: "Arimo", Arial, sans-serif;
    color: var(--ink);
  }
  .contact__person { font-size: 22px; }
  .contact__role { font-size: 15px; margin-bottom: 22px; }
  .contact__line { font-size: 17px; line-height: 1.25; }
  .contact__label { font-weight: 700; }
</style>
</head>
<body>
  <section class="card card--front" aria-label="Card front">
    <div class="card__band"></div>
    <div class="card__panel">
      <div class="card__band"></div>
      <h1 class="front__name">KL Estates</h1>
      <p class="front__email">projects.klestates@mailbox.com</p>
    </div>
  </section>

  <section class="card card--back" aria-label="Card back">
    <div class="card__band"></div>
    <div class="card__panel">
      <div class="back__mark"></div>
      <h2 class="back__name">KL Estates</h2>
      <div class="back__contact">
        <p class="contact__person">Daniel Hartley</p>
        <p class="contact__role">director</p>
        <p class="contact__line"><span class="contact__label">Phone:</span> (07) 3000 4821</p>
        <p class="contact__line"><span class="contact__label">Fax:</span> (07) 3000 4822</p>
        <p class="contact__line"><span class="contact__label">Email:</span> projects.klestates@mailbox.com</p>
        <p class="contact__line"><span class="contact__label">Postal:</span> PO Box 2754 Riverside North QLD 4170</p>
      </div>
    </div>
  </section>
</body>
</html>
```